New Zealand Luggage Importer Needs Business Cards

We need professional, creative and fashionable business cards created.
We are based in New Zealand and import and distribute high-end, quality, fashionable and durable luggage.
We pride ourselves on selling the very best quality luggage, second only to 1 brand (which we won't mention here)...we use the same manufacturer. However, our prices are much more reasonable.
Industry/Entity Type
Business
Contact Information for Business Card
Mark Dunsley
027 512 4068
3/17 Harlow Street, Pinecrest Flats, Auckland, 0614
PO Box 204377, Fernside, Auckland 0731
09-528-3916
sales@brivancases.co.nz / www.brivancases.co.nz

```html
<!DOCTYPE html>
<html lang="en">
<head>
<meta charset="utf-8">
<title>Brivan Cases — Business Card</title>
<link rel="stylesheet" href="https://fonts.googleapis.com/css2?family=Montserrat:wght@300;400;800&family=Open+Sans:wght@400;600&display=swap">
<style>
  :root {
    --ink: #231f20;
    --paper: #f4f4f4;
    --gold: #c9a544;
    --gold-light: #e6cf7e;
    --white: #ffffff;
    --stage: #e3e3e0;
    --photo-a: #e9e9e9;
    --photo-b: #cfcfcf;
  }
  * { box-sizing: border-box; margin: 0; padding: 0; }
  html, body { width: 1200px; height: 1200px; overflow: hidden; }
  body {
    background: var(--stage);
    display: flex;
    flex-direction: column;
    align-items: center;
    justify-content: center;
    gap: 52px;
    font-family: "Open Sans", sans-serif;
  }
  .card {
    position: relative;
    width: 900px;
    height: 514px;
    overflow: hidden;
    box-shadow: 0 10px 30px rgba(0,0,0,.18);
  }

  /* Front */
  .card-front { background: var(--paper); }
  .card-front .swoosh { position: absolute; inset: 0; width: 100%; height: 100%; }
  .brand {
    font-family: "Montserrat", sans-serif;
    font-weight: 800;
    letter-spacing: 2px;
    white-space: nowrap;
  }
  .card-front .brand {
    position: absolute;
    left: 70px; top: 52px;
    font-size: 46px;
    color: var(--ink);
  }
  .holder-name {
    position: absolute;
    left: 70px; top: 138px;
    font-family: "Montserrat", sans-serif;
    font-size: 46px;
    color: var(--ink);
    letter-spacing: 1px;
  }
  .holder-name .first { font-weight: 800; }
  .holder-name .last { font-weight: 300; }
  .product-photo {
    position: absolute;
    right: 40px; top: 250px;
    width: 330px; height: 210px;
    background: radial-gradient(ellipse at 55% 55%, var(--photo-b), var(--photo-a) 70%);
    border-radius: 4px;
  }
  .contact-list {
    position: absolute;
    left: 44px; top: 330px;
    list-style: none;
    color: var(--white);
    font-size: 21px;
    line-height: 36px;
  }
  .contact-list li { display: flex; align-items: center; gap: 12px; }
  .contact-list svg { width: 18px; height: 18px; fill: var(--gold); flex: none; }

  /* Back */
  .card-back { background: var(--ink); }
  .gold-frame {
    position: absolute;
    inset: 26px;
    border: 2px solid var(--gold);
  }
  .card-back .brand {
    position: absolute;
    top: 150px; left: 0; right: 0;
    text-align: center;
    font-size: 60px;
    color: var(--white);
  }
  .address {
    position: absolute;
    top: 300px; left: 0; right: 0;
    text-align: center;
    color: var(--white);
    font-size: 22px;
    line-height: 34px;
  }
  .address .web { color: var(--gold-light); font-weight: 600; }
</style>
</head>
<body>

<section class="card card-front">
  <svg class="swoosh" viewBox="0 0 900 514" preserveAspectRatio="none" aria-hidden="true">
    <path d="M0,292 C180,262 320,300 420,380 C510,452 610,505 760,514 L0,514 Z" fill="var(--gold)"/>
    <path d="M0,306 C180,278 315,318 412,396 C500,466 600,512 740,514 L0,514 Z" fill="var(--ink)"/>
  </svg>
  <div class="brand">BRIVAN CASES</div>
  <div class="holder-name"><span class="first">MARK</span> <span class="last">DUNSLEY</span></div>
  <div class="product-photo" role="img" aria-label="Photo of three black hard-shell suitcases with extended handles"></div>
  <ul class="contact-list">
    <li><svg viewBox="0 0 24 24"><path d="M6.6 10.8a15 15 0 0 0 6.6 6.6l2.2-2.2a1 1 0 0 1 1-.25 11.4 11.4 0 0 0 3.6.6 1 1 0 0 1 1 1V20a1 1 0 0 1-1 1A17 17 0 0 1 3 4a1 1 0 0 1 1-1h3.5a1 1 0 0 1 1 1c0 1.25.2 2.45.6 3.6a1 1 0 0 1-.25 1z"/></svg>027 512 4068</li>
    <li><svg viewBox="0 0 24 24"><path d="M7 1h10a2 2 0 0 1 2 2v18a2 2 0 0 1-2 2H7a2 2 0 0 1-2-2V3a2 2 0 0 1 2-2zm0 3v14h10V4zm5 15.5a1.2 1.2 0 1 0 0 2.4 1.2 1.2 0 0 0 0-2.4z"/></svg>09-528-3916</li>
    <li><svg viewBox="0 0 24 24"><path d="M2 21l21-9L2 3v7l15 2-15 2z"/></svg>sales@brivancases.co.nz</li>
    <li><svg viewBox="0 0 24 24"><path d="M12 2a10 10 0 1 0 0 20 10 10 0 0 0 0-20zm6.9 6h-3a15 15 0 0 0-1.4-3.9A8 8 0 0 1 18.9 8zM12 4c.8 1.2 1.5 2.5 1.9 4h-3.8c.4-1.5 1.1-2.8 1.9-4zM4.3 14a8 8 0 0 1 0-4h3.4a16 16 0 0 0 0 4zm.8 2h3a15 15 0 0 0 1.4 3.9A8 8 0 0 1 5.1 16zm3-8h-3a8 8 0 0 1 4.4-3.9A15 15 0 0 0 8.1 8zM12 20c-.8-1.2-1.5-2.5-1.9-4h3.8c-.4 1.5-1.1 2.8-1.9 4zm2.3-6H9.7a14 14 0 0 1 0-4h4.6a14 14 0 0 1 0 4zm.2 5.9a15 15 0 0 0 1.4-3.9h3a8 8 0 0 1-4.4 3.9zm1.8-5.9a16 16 0 0 0 0-4h3.4a8 8 0 0 1 0 4z"/></svg>www.brivancases.co.nz</li>
  </ul>
</section>

<section class="card card-back">
  <div class="gold-frame"></div>
  <div class="brand">BRIVAN CASES</div>
  <p class="address">
    3/17 Harlow Street, Pinecrest Flats, Auckland, 0614<br>
    PO Box 204377, Fernside, Auckland 0731<br>
    <span class="web">www.brivancases.co.nz</span>
  </p>
</section>

</body>
</html>
```